Security Warning Sign

We have an existing sign that needs an update. I have attached a picture of the current square sign. We need to maintain the same wording. It needs to be professional and appropriate to attach to our customers fence. Also attached is a copy of our building sign which may lend some inspiration and hopefully the ai format will assist. The final sign will be 600mm x 600mmOur website is www.halvorngate.com.au

```html
<!DOCTYPE html>
<html lang="en">
<head>
<meta charset="utf-8">
<title>Security Warning Sign – Halvorngate Security Services</title>
<link href="https://fonts.googleapis.com/css2?family=Jost:wght@600;700&family=Oswald:wght@600&display=swap" rel="stylesheet">
<style>
  :root {
    --sign-orange: #f28634;
    --ink: #1b1b1b;
    --panel-tone-light: #f7f7f7;
    --panel-tone-mid: #eeeeee;
    --rule-grey: #b9b9b9;
  }
  html, body {
    margin: 0;
    padding: 0;
    width: 1200px;
    height: 1200px;
    overflow: hidden;
    background: #ffffff;
  }
  .sign {
    position: relative;
    width: 1200px;
    height: 1200px;
    overflow: hidden;
    font-family: "Jost", "Futura", sans-serif;
  }
  .sign__backdrop {
    position: absolute;
    inset: 0;
    background: linear-gradient(135deg, var(--panel-tone-light), var(--panel-tone-mid));
  }
  .sign__headline {
    position: absolute;
    top: 92px;
    left: 0;
    width: 100%;
    margin: 0;
    text-align: center;
    font-weight: 700;
    font-size: 200px;
    line-height: 200px;
    letter-spacing: 2px;
    color: var(--sign-orange);
  }
  .sign__message {
    position: absolute;
    top: 378px;
    left: 0;
    width: 100%;
    margin: 0;
    text-align: center;
    font-weight: 700;
    font-size: 94px;
    line-height: 107px;
    color: var(--ink);
    text-transform: uppercase;
  }
  .sign__footer-shapes {
    position: absolute;
    left: 0;
    top: 1000px;
    width: 1200px;
    height: 200px;
  }
  .brand {
    position: absolute;
    left: 70px;
    top: 1016px;
    display: flex;
    align-items: center;
    gap: 20px;
  }
  .brand__mark {
    width: 134px;
    height: 134px;
    border-radius: 50%;
    background: var(--sign-orange);
  }
  .brand__name {
    margin: 0;
    font-weight: 700;
    font-size: 33px;
    line-height: 36px;
    letter-spacing: 1px;
    color: var(--ink);
  }
  .sign__phone {
    position: absolute;
    left: 600px;
    top: 1030px;
    width: 580px;
    margin: 0;
    text-align: center;
    font-family: "Oswald", "Arial Narrow", sans-serif;
    font-weight: 600;
    font-size: 104px;
    line-height: 160px;
    letter-spacing: -2px;
    color: #ffffff;
  }
</style>
</head>
<body>
  <main class="sign">
    <div class="sign__backdrop" role="img" aria-label="Light grey diagonal hazard stripe background"></div>

    <h1 class="sign__headline">WARNING</h1>
    <p class="sign__message">Electronic<br>Surveillance and<br>Recording<br>Devices installed<br>in this area</p>

    <svg class="sign__footer-shapes" viewBox="0 1000 1200 200" aria-hidden="true">
      <polygon points="0,1186 430,1186 422,1200 0,1200" fill="var(--rule-grey)"/>
      <polygon points="526,1060 540,1060 451,1200 437,1200" fill="var(--rule-grey)"/>
      <polygon points="566,1025 578,1025 468,1200 456,1200" fill="var(--sign-orange)"/>
      <polygon points="596,1025 1200,1025 1200,1200 486,1200" fill="var(--sign-orange)"/>
    </svg>

    <div class="brand">
      <div class="brand__mark"></div>
      <p class="brand__name">HALVORNGATE<br>SECURITY<br>SERVICES</p>
    </div>

    <p class="sign__phone">1300 415 276</p>
  </main>
</body>
</html>
```